We are a Yacht Charter Broker servicing VIP clients on booking sailing catamarans and motor yacht...

We are looking for a wildly creative website to attract high net worth clients to work with us in booking their dream yacht vacation. A site that you think is 5 years ahead of its time. Sexy, modern and unique. Our company name is BRELLAVON. Our colors are navy blue and silver.
BLUE:
RGBB 0/44/92
CMYC 100/86/36/31
SILVER:
RGB 152/163/173
CMYK 43/29/25/0

HEX 98a3ad

Target Market(s)

High net worth people in need of white glove brokerage serving in finding and booking their dream yacht for a vacation of a lifetime.

Coding

Coded - Design and coding required

Number of Pages Required

1 page

Requirements
Must have
• Mobile friendly.
• Wildly creative and different. A website that we would expect to see 5 years from now.
• Pictures of yachts and or people on yachts. Palm tree landscapes.
• pictures of high end food related to the VIP yacht experience.
Nice to have
• Anything you feel would sell the yacht charter experience.
Should not have
• Nothing comes to mind.

```html
<!DOCTYPE html>
<html lang="en">
<head>
<meta charset="utf-8">
<title>Brellavon – Yacht Charter Broker</title>
<link href="https://fonts.googleapis.com/css2?family=Cinzel:wght@400;600&family=Lora:wght@400;600&display=swap" rel="stylesheet">
<style>
:root{
  --navy:#002c5c;
  --navy-deep:#0a2550;
  --navy-mid:#123a72;
  --silver:#98a3ad;
  --silver-light:#c8d0d8;
  --white:#ffffff;
  --head:'Cinzel',serif;
  --body:'Lora',serif;
}
*{box-sizing:border-box;margin:0;padding:0}
html,body{width:1200px;height:3939px;overflow:hidden}
body{position:relative;background:linear-gradient(#0e3068,#0c2c60 40%,#0b2a5c);font-family:var(--body);color:var(--white)}
.abs{position:absolute}
.heading{font-family:var(--head);font-weight:400;letter-spacing:4px;text-align:center;width:1200px;font-size:44px;color:var(--white)}
.btn{display:inline-block;font-family:var(--head);font-size:11px;letter-spacing:1px;text-align:center;background:var(--silver);color:var(--navy);padding:9px 0;box-shadow:0 3px 6px rgba(0,0,0,.35)}
.lorem{font-size:11px;line-height:19px;color:#dfe6ef;text-align:center}

/* header */
.site-header{top:0;left:0;width:1200px;height:84px;background:var(--white);z-index:2}
.brand{left:110px;top:18px;font-family:var(--head);font-size:30px;letter-spacing:4px;color:var(--navy)}
.brand-tag{left:150px;top:56px;font-family:var(--head);font-size:8px;letter-spacing:2px;color:var(--silver)}
.main-nav{left:567px;top:34px;display:flex;gap:30px;font-family:var(--head);font-size:11px;color:var(--navy)}
.search-icon{left:1070px;top:30px}

/* hero */
.hero{top:84px;left:0;width:1200px;height:740px;background:
  radial-gradient(ellipse 40% 8% at 30% 41%,rgba(190,212,236,.55),rgba(190,212,236,0)),
  linear-gradient(180deg,#4a7fc0 0%,#6795cd 30%,#a3c0e2 39.5%,#4a79b6 41%,#2f62a2 52%,#1c4b8c 70%,#123d7a 86%,#0e3068 100%)}
.hero-photo{top:84px;left:740px;width:460px;height:560px;background:
  radial-gradient(ellipse 75% 26% at 70% 66%,#f6f8fa 0%,#e2e9f0 40%,rgba(226,233,240,0) 100%),
  radial-gradient(ellipse 30% 22% at 52% 34%,#efe2d6 0%,#d9c6c4 40%,rgba(217,198,196,0) 100%),
  radial-gradient(ellipse 22% 18% at 70% 30%,#f1c9d6 0%,rgba(241,201,214,0) 100%),
  linear-gradient(200deg,rgba(230,238,246,.6) 0%,rgba(120,160,210,0) 45%),
  radial-gradient(ellipse 60% 30% at 60% 85%,rgba(40,90,170,.7),rgba(40,90,170,0))}
.hero-eyebrow{left:110px;top:196px;font-family:var(--head);font-size:24px;letter-spacing:2px}
.hero-title{left:108px;top:222px;font-family:var(--head);font-weight:400;font-size:71px;line-height:80px;letter-spacing:3px}
.hero-tabs{left:115px;top:412px;display:flex;gap:18px}
.hero-tabs .tab{width:135px;height:34px;line-height:34px;font-family:var(--head);font-size:10px;text-align:center;box-shadow:0 3px 6px rgba(0,0,0,.3)}
.tab-active{background:var(--white);color:var(--navy)}
.tab-plain{background:#2b4f86;color:var(--white);width:105px!important}
.scroll-cue{left:589px;top:655px}

/* sea band behind fleet */
.sea-band{top:1390px;left:0;width:1200px;height:640px;background:
  radial-gradient(ellipse 60% 45% at 50% 45%,#2a5a98 0%,#1b4583 45%,rgba(14,48,104,0) 100%),
  linear-gradient(180deg,rgba(14,48,104,0),#163f7c 40%,rgba(14,48,104,0))}

/* welcome */
.welcome-eyebrow{left:220px;top:868px;width:426px;text-align:center;font-family:var(--head);font-size:13px;letter-spacing:2px}
.welcome-name{left:220px;top:888px;width:426px;text-align:center;font-family:var(--head);font-size:40px;letter-spacing:6px}
.welcome-tag{left:220px;top:953px;width:426px;text-align:center;font-family:var(--head);font-size:12px;letter-spacing:1px}
.welcome-text{left:220px;top:982px;width:426px}
.welcome-btn{left:328px;top:1132px;width:170px}
.welcome-photo{left:698px;top:848px;width:289px;height:334px;border:4px solid var(--white);box-shadow:0 10px 25px rgba(0,0,0,.45);background:
  radial-gradient(ellipse 45% 30% at 40% 75%,#f3f3f1 0%,#dcdedf 50%,rgba(220,222,223,0) 100%),
  radial-gradient(ellipse 40% 35% at 62% 38%,#2d4a7a 0%,rgba(45,74,122,0) 100%),
  radial-gradient(ellipse 30% 20% at 40% 35%,#e6c8b0 0%,rgba(230,200,176,0) 100%),
  linear-gradient(0deg,#8a6a4e 0%,#a57d58 18%,rgba(165,125,88,0) 30%),
  linear-gradient(180deg,#a9cdea 0%,#d7e6f1 50%,#c4ced8 100%)}

/* stats */
.stats{top:1255px;left:200px;width:800px;display:flex}
.stat{flex:1;text-align:center;border-right:1px solid rgba(152,163,173,.35);height:120px}
.stat:last-child{border-right:none}
.stat-num{font-family:var(--head);font-size:34px;margin-top:24px}
.stat-num small{font-size:18px}
.stat-label{font-family:var(--head);font-size:10px;letter-spacing:1px;margin-top:8px}

/* fleets */
.fleet-card{width:368px}
.fleet-photo{width:368px;height:210px;border:4px solid var(--white);box-shadow:0 8px 20px rgba(0,0,0,.4)}
.fleet-title{font-family:var(--head);font-weight:400;font-size:22px;text-align:center;margin-top:24px;letter-spacing:2px}
.fleet-text{margin-top:4px}
.fleet-price{text-align:center;font-family:var(--head);font-size:12px;margin-top:6px}
.fleet-price b{font-size:30px;font-weight:400}
.fleet-card .btn{display:block;width:100px;margin:12px auto 0}

/* steps */
.steps-line{top:2050px;left:0}
.step{width:140px;text-align:center}
.step-ring{width:136px;height:136px;border-radius:50%;border:3px solid var(--silver-light);background:var(--white);position:relative;box-shadow:0 6px 16px rgba(0,0,0,.35)}
.step-ring svg{position:absolute;left:33px;top:33px}
.step-dot{position:absolute;left:58px;bottom:-9px;width:16px;height:16px;border-radius:50%;background:var(--silver);border:3px solid var(--navy)}
.step-label{font-family:var(--head);font-size:11px;letter-spacing:.5px;white-space:nowrap;width:200px;margin-left:-30px}

/* offers */
.offer{width:245px;height:232px;background:var(--white);color:var(--navy);box-shadow:0 6px 16px rgba(0,0,0,.4);overflow:hidden}
.offer-photo{width:237px;height:150px;margin:4px}
.offer-badge{position:absolute;right:-26px;top:14px;width:110px;transform:rotate(45deg);background:#5c6773;color:var(--white);font-family:var(--head);font-size:9px;text-align:center;padding:3px 0}
.offer-name{position:absolute;left:12px;top:168px;font-family:var(--head);font-size:12px}
.offer-meta{position:absolute;left:12px;top:198px;display:flex;gap:14px;font-size:11px;color:#555;align-items:center}
.offer-price{position:absolute;right:14px;top:182px;font-family:var(--head);font-size:24px}
.offer-price small{font-size:13px}

/* video */
.video-band{top:2757px;left:0;width:1200px;height:368px;background:
  radial-gradient(ellipse 40% 22% at 48% 36%,#f2f3f3 0%,#c9ced3 45%,rgba(201,206,211,0) 100%),
  radial-gradient(ellipse 18% 30% at 62% 60%,#d6b49a 0%,rgba(214,180,154,0) 100%),
  radial-gradient(ellipse 30% 20% at 35% 55%,#3b4650 0%,rgba(59,70,80,0) 100%),
  linear-gradient(180deg,#c3ccd4 0%,#9fb1c2 28%,#6f8ea6 42%,#2aa3b7 55%,#19a4b4 70%,#0f8796 100%)}
.play{left:570px;top:2916px}

/* testimonials */
.quote{width:368px;height:104px;background:rgba(4,24,56,.75);padding:12px 14px;box-shadow:0 6px 14px rgba(0,0,0,.35)}
.quote p{font-size:10.5px;line-height:16px;color:#dfe6ef;width:245px}
.quote-name{font-family:var(--head);font-size:12px;margin-top:8px}
.quote-name span{color:#e9c35a;font-size:10px;letter-spacing:1px}
.quote-mark{position:absolute;right:18px;top:10px;font-family:var(--head);font-size:48px;color:rgba(152,163,173,.35);line-height:1}
.avatar{position:absolute;width:94px;height:94px;border-radius:50%;border:3px solid var(--white)}
.slider-arrow{font-size:18px;color:var(--silver-light)}

/* newsletter */
.newsletter{top:3480px;left:0;width:1200px;height:73px;background:#0a2248}
.news-label{left:255px;top:24px;font-family:var(--head);font-size:20px;letter-spacing:2px}
.news-input{left:622px;top:20px;width:368px;height:32px;border-radius:16px;background:#2a3f63;color:#9aa8bb;font-size:10px;padding:9px 16px}
.news-send{left:960px;top:24px;width:24px;height:24px;border-radius:50%;background:var(--silver-light)}

/* footer */
.site-footer{top:3553px;left:0;width:1200px;height:360px;background:linear-gradient(#0f2f66,#0b2656)}
.links-title{left:210px;top:3618px;font-family:var(--head);font-size:13px}
.links{left:210px;top:3655px;list-style:none;font-size:11px;line-height:26px}
.links li::before{content:"›";margin-right:10px}
.foot-brand{left:373px;top:3612px;font-family:var(--head);font-size:30px;letter-spacing:4px}
.foot-tag{left:400px;top:3650px;font-family:var(--head);font-size:8px;letter-spacing:2px;color:var(--silver-light)}
.contact{left:373px;font-size:11px;display:flex;gap:10px;align-items:flex-start;line-height:15px}
.map{left:736px;top:3567px;width:247px;height:247px;border-radius:50%;border:5px solid var(--white);background:
  linear-gradient(35deg,rgba(255,255,255,0) 47%,rgba(200,208,216,.25) 48%,rgba(200,208,216,.25) 52%,rgba(255,255,255,0) 53%),
  radial-gradient(#35588a,#1b3961)}
.bottom-bar{top:3913px;left:0;width:1200px;height:26px;background:#082050;font-size:9px;font-family:var(--head)}
.social{display:flex;gap:4px}
.social i{display:block;width:14px;height:14px;background:var(--silver-light)}
</style>
</head>
<body>

<section class="hero abs" role="img" aria-label="Open sea under a bright blue sky, the water deepening into navy"></section>
<div class="hero-photo abs" role="img" aria-label="Couple relaxing on the bow of a white sailing yacht"></div>

<header class="site-header abs">
  <div class="brand abs">BRELLAVON</div>
  <div class="brand-tag abs">YACHT CHARTER BROKER</div>
  <nav class="main-nav abs"><span>ABOUT US</span><span>CATAMARANS</span><span>YACHT</span><span>SPECIALS</span><span>ADVICE</span><span>CONTACT US</span></nav>
  <svg class="search-icon abs" width="16" height="16" viewBox="0 0 16 16"><circle cx="6.5" cy="6.5" r="5" fill="none" stroke="#002c5c" stroke-width="2"/><line x1="10" y1="10" x2="15" y2="15" stroke="#002c5c" stroke-width="2"/></svg>
</header>

<div class="hero-eyebrow abs">EXPERIENCE THE</div>
<h1 class="hero-title abs">LUXURIOUS<br>SAILING</h1>
<div class="hero-tabs abs"><span class="tab tab-active">CATAMARANS</span><span class="tab tab-plain">YACHT</span></div>
<svg class="scroll-cue abs" width="20" height="32" viewBox="0 0 20 32"><rect x="2" y="2" width="16" height="28" rx="8" fill="none" stroke="#c8d0d8" stroke-width="2"/><line x1="10" y1="8" x2="10" y2="13" stroke="#c8d0d8" stroke-width="2"/></svg>

<section class="welcome">
  <div class="welcome-eyebrow abs">WELCOME TO</div>
  <div class="welcome-name abs">BRELLAVON</div>
  <div class="welcome-tag abs">YACHT CHARTER BROKER</div>
  <p class="welcome-text lorem abs">Lorem ipsum dolor sit amet, consectetur adipiscing elit. Integer tempus sapien sed tempor vestibulum. Vestibulum vel lacus, hendrerit et interdum a, porta sit amet leo. Mauris vitae pellentesque purus. Donec rhoncus orci eget odio egestas, vel malesuada felis volutpat. Duis turpis magna, sagittis rhoncus ex sit amet, eleifend tristique.</p>
  <span class="welcome-btn btn abs">FIND RIGHT BROKER</span>
  <div class="welcome-photo abs" role="img" aria-label="Smiling couple seated together on a teak yacht deck"></div>
</section>

<section class="stats abs">
  <div class="stat"><div class="stat-num">100+</div><div class="stat-label">YACHT SELECTIONS</div></div>
  <div class="stat"><div class="stat-num"><small>NO.</small>01</div><div class="stat-label">CHARTER BROKER</div></div>
  <div class="stat"><div class="stat-num">521+</div><div class="stat-label">SATISFIED CUSTOMERS</div></div>
  <div class="stat"><div class="stat-num">75+</div><div class="stat-label">LOCATIONS SERVING</div></div>
</section>

<div class="sea-band abs" role="img" aria-label="Deep blue open sea surface"></div>

<h2 class="heading abs" style="top:1425px;left:0">FIND YOUR SAIL</h2>
<article class="fleet-card abs" style="left:210px;top:1502px">
  <div class="fleet-photo" role="img" aria-label="White catamaran seen from above on turquoise water" style="background:radial-gradient(ellipse 50% 40% at 55% 45%,#f4f5f5 0%,#d9dee2 45%,rgba(217,222,226,0) 100%),radial-gradient(ellipse 30% 25% at 35% 70%,#e6e9ec 0%,rgba(230,233,236,0) 100%),linear-gradient(160deg,#8fd0e0 0%,#3fa3bf 45%,#1d7a99 100%)"></div>
  <h3 class="fleet-title">CATAMARANS</h3>
  <p class="fleet-text lorem">Lorem ipsum dolor sit amet, consectetur adipiscing elit. Integer tempus sapien sed tempor vestibulum. Vestibulum vel lacus.</p>
  <div class="fleet-price">FROM <b>700$</b> / WEEK</div>
  <span class="btn">FIND NOW</span>
</article>
<article class="fleet-card abs" style="left:622px;top:1502px">
  <div class="fleet-photo" role="img" aria-label="White motor yacht cruising on blue sea" style="background:radial-gradient(ellipse 45% 22% at 50% 58%,#ffffff 0%,#e4e8ec 50%,rgba(228,232,236,0) 100%),linear-gradient(180deg,#7fc1ec 0%,#b9def3 38%,#e6f2f8 48%,#2f86c4 56%,#1b63a6 100%)"></div>
  <h3 class="fleet-title">YACHT</h3>
  <p class="fleet-text lorem">Lorem ipsum dolor sit amet, consectetur adipiscing elit. Integer tempus sapien sed tempor vestibulum. Vestibulum vel lacus.</p>
  <div class="fleet-price">FROM <b>500$</b> / WEEK</div>
  <span class="btn">FIND NOW</span>
</article>

<h2 class="heading abs" style="top:1970px;left:0">BOOK EASILY</h2>
<svg class="steps-line abs" width="1200" height="200" viewBox="0 0 1200 200"><path d="M160 140 Q 230 90 297 82 Q 400 40 494 55 Q 600 110 704 85 Q 800 40 901 48 Q 1000 55 1070 125" fill="none" stroke="rgba(200,208,216,.45)" stroke-width="2"/><circle cx="160" cy="140" r="5" fill="#98a3ad"/><circle cx="1070" cy="125" r="5" fill="#98a3ad"/></svg>
<div class="step abs" style="left:227px;top:2064px"><div class="step-ring"><svg width="64" height="64" viewBox="0 0 64 64" role="img" aria-label="Boat icon"><path d="M10 40 L54 40 L46 50 L18 50 Z" fill="none" stroke="#1d3560" stroke-width="2.5"/><path d="M30 12 L30 38 M30 14 L46 36 L30 36" fill="none" stroke="#1d3560" stroke-width="2.5"/><path d="M8 56 Q16 52 24 56 T40 56 T56 56" fill="none" stroke="#1d3560" stroke-width="2"/></svg><div class="step-dot"></div></div><div class="step-label" style="margin-top:26px">FIND RIGHT FLEET</div></div>
<div class="step abs" style="left:424px;top:2022px"><div class="step-ring"><svg width="64" height="64" viewBox="0 0 64 64" role="img" aria-label="Card payment icon"><rect x="8" y="16" width="40" height="28" rx="3" fill="none" stroke="#1d3560" stroke-width="2.5"/><line x1="8" y1="24" x2="48" y2="24" stroke="#1d3560" stroke-width="4"/><rect x="38" y="36" width="18" height="14" rx="2" fill="#fff" stroke="#1d3560" stroke-width="2.5"/><path d="M42 36 V32 a5 5 0 0 1 10 0 V36" fill="none" stroke="#1d3560" stroke-width="2.5"/></svg><div class="step-dot"></div></div><div class="step-label" style="margin-top:26px">PAY SECURED ONLINE</div></div>
<div class="step abs" style="left:634px;top:2064px"><div class="step-ring"><svg width="64" height="64" viewBox="0 0 64 64" role="img" aria-label="Booking confirmed tick icon"><circle cx="32" cy="32" r="22" fill="none" stroke="#1d3560" stroke-width="2.5"/><path d="M21 32 L29 40 L44 24" fill="none" stroke="#1d3560" stroke-width="3"/></svg><div class="step-dot"></div></div><div class="step-label" style="margin-top:26px">YOUR FLEET NOW BOOKED</div></div>
<div class="step abs" style="left:831px;top:2022px"><div class="step-ring"><svg width="64" height="64" viewBox="0 0 64 64" role="img" aria-label="Sun icon"><circle cx="32" cy="32" r="10" fill="none" stroke="#1d3560" stroke-width="2.5"/><path d="M32 8 V16 M32 48 V56 M8 32 H16 M48 32 H56 M15 15 L20 20 M44 44 L49 49 M49 15 L44 20 M20 44 L15 49" stroke="#1d3560" stroke-width="2.5"/></svg><div class="step-dot"></div></div><div class="step-label" style="margin-top:26px">ENJOY THE HOLIDAY!</div></div>
<span class="btn abs" style="left:522px;top:2282px;width:156px">GET STARTED NOW</span>

<h2 class="heading abs" style="top:2376px;left:0">OFFERS &amp; DEALS</h2>
<article class="offer abs" style="left:210px;top:2455px">
  <div class="offer-photo" role="img" aria-label="Luxury motor yacht at anchor" style="background:radial-gradient(ellipse 60% 35% at 50% 55%,#ffffff 0%,#dfe4e9 50%,rgba(223,228,233,0) 100%),linear-gradient(180deg,#9cc4e2 0%,#c9dcea 40%,#3b7fb2 60%,#1e5a8f 100%)"></div>
  <span class="offer-badge">20% OFF</span>
  <div class="offer-name">BOAT NAME HERE</div>
  <div class="offer-meta"><span>▢ 07</span><span>▭ 04</span></div>
  <div class="offer-price">450 <small>$</small></div>
</article>
<article class="offer abs" style="left:483px;top:2455px">
  <div class="offer-photo" role="img" aria-label="Flybridge yacht with sun canopy" style="background:radial-gradient(ellipse 30% 14% at 48% 22%,#f3e6a2 0%,rgba(243,230,162,0) 100%),radial-gradient(ellipse 55% 28% at 50% 55%,#ffffff 0%,#e4e7ea 50%,rgba(228,231,234,0) 100%),linear-gradient(180deg,#86c2ea 0%,#bfe0f2 35%,#2b8cc6 55%,#1c6aa6 100%)"></div>
  <span class="offer-badge">20% OFF</span>
  <div class="offer-name">BOAT NAME HERE</div>
  <div class="offer-meta"><span>▢ 05</span><span>▭ 03</span></div>
  <div class="offer-price">350 <small>$</small></div>
</article>
<article class="offer abs" style="left:748px;top:2455px">
  <div class="offer-photo" role="img" aria-label="Sleek yacht cruising at speed" style="background:radial-gradient(ellipse 60% 22% at 50% 52%,#f5f6f7 0%,#c9d0d7 50%,rgba(201,208,215,0) 100%),linear-gradient(180deg,#b5cde2 0%,#dbe5ee 35%,#3a5f8e 55%,#173f73 100%)"></div>
  <span class="offer-badge">20% OFF</span>
  <div class="offer-name">BOAT NAME HERE</div>
  <div class="offer-meta"><span>▢ 09</span><span>▭ 05</span></div>
  <div class="offer-price">550 <small>$</small></div>
</article>

<section class="video-band abs" role="img" aria-label="Swimmer in turquoise water beside a large motor yacht"></section>
<svg class="play abs" width="60" height="60" viewBox="0 0 60 60"><circle cx="30" cy="30" r="29" fill="#ffffff"/><circle cx="30" cy="30" r="24" fill="#0b2a5c"/><path d="M25 19 L41 30 L25 41 Z" fill="#ffffff"/></svg>

<h2 class="heading abs" style="top:3182px;left:0">CLIENT TESTIMONIALS</h2>
<span class="slider-arrow abs" style="left:175px;top:3300px">‹</span>
<span class="slider-arrow abs" style="left:1008px;top:3300px">›</span>
<div class="quote abs" style="left:215px;top:3264px">
  <p>Lorem ipsum dolor sit amet, consectetur adipiscing elit fermentum. Lorem eu interdum tempusid est accumsan dui, molestie consectetur.</p>
  <div class="quote-name">MARA QUILL <span>★★★★★</span></div>
  <span class="quote-mark">“</span>
</div>
<div class="avatar" role="img" aria-label="Client portrait" style="left:474px;top:3330px;background:radial-gradient(circle at 50% 40%,#d9c2b4,#8a6f66 70%,#f0f0f0 71%)"></div>
<div class="quote abs" style="left:609px;top:3264px">
  <p>Lorem ipsum dolor sit amet, consectetur adipiscing elit fermentum. Lorem eu interdum tempusid est accumsan dui, molestie consectetur.</p>
  <div class="quote-name">OWEN HALE <span>★★★★★</span></div>
  <span class="quote-mark">“</span>
</div>
<div class="avatar" role="img" aria-label="Client portrait" style="left:868px;top:3330px;background:radial-gradient(circle at 50% 38%,#e2c7b3,#b99a86 55%,#3b4d6a 70%)"></div>

<section class="newsletter abs">
  <svg class="abs" style="left:210px;top:20px" width="34" height="32" viewBox="0 0 34 32"><rect x="2" y="6" width="26" height="18" fill="none" stroke="#fff" stroke-width="2"/><path d="M2 6 L15 16 L28 6" fill="none" stroke="#fff" stroke-width="2"/></svg>
  <div class="news-label abs">STAY UP TO DATE WITH US:</div>
  <div class="news-input abs">Enter your email...</div>
  <svg class="news-send abs" viewBox="0 0 24 24"><path d="M6 12 L18 6 L14 18 L12 13 Z" fill="#0a2248"/></svg>
</section>

<footer class="site-footer abs"></footer>
<div class="links-title abs">QUICK LINKS</div>
<ul class="links abs"><li>Home</li><li>About Us</li><li>Catamarans</li><li>Yacht</li><li>Specials</li><li>Advice</li><li>Contact</li></ul>
<div class="foot-brand abs">BRELLAVON</div>
<div class="foot-tag abs">YACHT CHARTER BROKER</div>
<div class="contact abs" style="top:3676px"><svg width="12" height="16" viewBox="0 0 12 16"><path d="M6 1 A5 5 0 0 1 11 6 C11 10 6 15 6 15 C6 15 1 10 1 6 A5 5 0 0 1 6 1Z" fill="#fff"/><circle cx="6" cy="6" r="2" fill="#0f2f66"/></svg><span>Please Write Your Address<br>here with State Zip, Country</span></div>
<div class="contact abs" style="top:3724px"><svg width="14" height="10" viewBox="0 0 14 10"><rect x="0" y="0" width="14" height="10" fill="#fff"/><path d="M0 0 L7 6 L14 0" fill="none" stroke="#0f2f66"/></svg><span>info@brellavon.com</span></div>
<div class="contact abs" style="top:3758px"><svg width="12" height="12" viewBox="0 0 12 12"><path d="M2 1 L4.5 1 L5.5 4 L4 5 Q5.5 7.5 7 8 L8 6.5 L11 7.5 L11 10 Q5 11 1 3 Z" fill="#fff"/></svg><span>Call : <b>1800-555-0142</b></span></div>
<div class="map abs" role="img" aria-label="Street map showing office location"></div>

<div class="bottom-bar abs">
  <span class="abs" style="left:210px;top:8px">© COPYRIGHT 2018 BRELLAVON. ALL RIGHT RESERVED</span>
  <span class="abs" style="left:788px;top:8px">FOLLOW US ON SOCIAL</span>
  <div class="social abs" style="left:900px;top:6px"><i></i><i></i><i></i><i></i><i></i></div>
</div>

</body>
</html>
```